Upmark Velo

We are a new start up company selling (online) innovative cycling products.
Being a new player in the market a modern eye catching logo would be good.
Initially selling safety tail lights with blinkers & modern designed cycling gloves and eventually extending our range into cycling clothing. Many of our products will have a safety theme.

Please see logo attached.
Updates

Project Deadline Extended
Reason: I have extended deadline because i have just received the Logo to be used.

Target Market(s)

We will be target marketing to the young 20-30year old trendy commuter cyclists to the 40 - 60 year old weekend road riders with there immaculate color coordinated road bikes & clothing.

Industry/Entity Type

Safety

Requirements
Must have
• Name: Liam Beck
Line for Mobile No. 0468 923 051
Line for email Address: liam@upmarkvelo.com.au
3 Lines for Postal Address: PO Box 3826
Harlow Vale Crossing
NSW 2157
Website: www.upmarkvelo.com.au

```html
<!DOCTYPE html>
<html lang="en">
<head>
<meta charset="utf-8">
<title>Upmark Velo – Business Card</title>
<link href="https://fonts.googleapis.com/css2?family=Open+Sans:wght@400;600;700;800&display=swap" rel="stylesheet">
<style>
  :root{
    --ink:#2b2a2b;
    --orange:#e98a2c;
    --paper:#ffffff;
    --backdrop:#d9d9d9;
  }
  *{box-sizing:border-box;margin:0;padding:0}
  html,body{width:1200px;height:720px;overflow:hidden}
  body{
    background:var(--backdrop);
    font-family:"Open Sans",Arial,sans-serif;
    display:flex;align-items:center;justify-content:center;gap:40px;
  }
  .card{
    position:relative;width:560px;height:320px;background:var(--paper);
    overflow:hidden;box-shadow:0 6px 18px rgba(0,0,0,.18);
  }
  .card-shapes{position:absolute;inset:0}

  /* brand lockup */
  .brand{position:absolute;display:flex;align-items:center;gap:10px}
  .brand-dot{width:18px;height:18px;border-radius:50%;background:var(--orange)}
  .brand-name{font-weight:600;font-size:34px;color:var(--ink);letter-spacing:-.5px}

  /* front */
  .front .brand{left:40px;top:118px}
  .holder-name{
    position:absolute;right:40px;top:10px;color:var(--paper);
    font-weight:800;font-size:22px;
  }
  .role{
    position:absolute;right:28px;top:66px;color:var(--paper);
    font-weight:800;font-size:17px;
  }
  .contact-list{
    position:absolute;left:346px;top:96px;width:200px;list-style:none;
  }
  .contact-list li{
    display:flex;align-items:flex-start;gap:7px;
    color:var(--paper);font-weight:600;font-size:11.5px;line-height:1.35;
    padding:5px 0;border-bottom:2px solid var(--paper);
  }
  .contact-list li:last-child{border-bottom:none}
  .contact-list svg{flex:0 0 13px;width:13px;height:13px;margin-top:1px}

  /* back */
  .web-vertical{
    position:absolute;left:30px;top:24px;
    transform-origin:left top;transform:rotate(90deg) translateY(-22px);
    color:var(--orange);font-weight:600;font-size:12px;white-space:nowrap;
  }
  .offer-title{
    position:absolute;left:96px;top:9px;color:var(--paper);
    font-weight:800;font-size:19px;
  }
  .offer-list{
    position:absolute;left:96px;top:68px;list-style:none;
    color:var(--orange);font-weight:600;font-size:14px;line-height:1.55;
  }
  .offer-list li::before{content:"+ ";color:var(--ink);font-weight:700}
  .back .brand{right:40px;bottom:62px}
</style>
</head>
<body>

  <!-- front -->
  <section class="card front">
    <svg class="card-shapes" viewBox="0 0 560 320" aria-hidden="true">
      <path d="M230 0 H560 V48 H300 Q278 48 268 28 Q256 0 230 0 Z" fill="var(--ink)"/>
      <path d="M360 56 H560 V246 H330 V86 Q330 56 360 56 Z" fill="var(--orange)"/>
      <rect x="0" y="260" width="560" height="4" fill="var(--orange)"/>
      <path d="M0 270 H560 V320 H0 Z" fill="var(--ink)"/>
    </svg>

    <div class="holder-name">Liam Beck</div>

    <div class="brand">
      <span class="brand-dot"></span>
      <span class="brand-name">Upmark Velo</span>
    </div>

    <div class="role">Owner</div>
    <ul class="contact-list">
      <li>
        <svg viewBox="0 0 14 14" fill="none" stroke="#fff" stroke-width="1.4"><rect x="4" y="1" width="6" height="12" rx="1"/><line x1="6" y1="11" x2="8" y2="11"/></svg>
        0468 923 051
      </li>
      <li>
        <svg viewBox="0 0 14 14" fill="none" stroke="#fff" stroke-width="1.4"><rect x="1" y="3" width="12" height="8"/><path d="M1 3 L7 8 L13 3"/></svg>
        liam@upmarkvelo.com.au
      </li>
      <li>
        <svg viewBox="0 0 14 14" fill="none" stroke="#fff" stroke-width="1.4"><rect x="1" y="2" width="12" height="8"/><line x1="5" y1="12.5" x2="9" y2="12.5"/></svg>
        www.upmarkvelo.com.au
      </li>
      <li>
        <svg viewBox="0 0 14 14"><path d="M7 1 C4 1 2.5 3 2.5 5.3 C2.5 8.5 7 13 7 13 C7 13 11.5 8.5 11.5 5.3 C11.5 3 10 1 7 1 Z" fill="#fff"/><circle cx="7" cy="5.3" r="1.7" fill="var(--orange)"/></svg>
        <span>PO Box 3826<br>Harlow Vale Crossing<br>NSW 2157</span>
      </li>
    </ul>
  </section>

  <!-- back -->
  <section class="card back">
    <svg class="card-shapes" viewBox="0 0 560 320" aria-hidden="true">
      <rect x="0" y="0" width="64" height="320" fill="var(--ink)"/>
      <path d="M0 200 H50 Q80 200 80 230 V320 H0 Z" fill="var(--orange)"/>
      <path d="M64 0 H340 Q360 0 370 22 Q380 44 400 44 H64 Z" fill="var(--ink)"/>
      <path d="M64 296 H560 V320 H64 Z" fill="var(--ink)"/>
      <rect x="64" y="290" width="496" height="3" fill="var(--orange)"/>
    </svg>

    <div class="web-vertical">www.upmarkvelo.com.au</div>
    <div class="offer-title">We Offer</div>
    <ul class="offer-list">
      <li>Safety Tail Lights With Blinkers</li>
      <li>Modern Designed Cycling Gloves</li>
      <li>Cycling Clothing</li>
      <li>Many of our products will<br>&nbsp;&nbsp;&nbsp;have a safety theme</li>
    </ul>

    <div class="brand">
      <span class="brand-dot"></span>
      <span class="brand-name">Upmark Velo</span>
    </div>
  </section>

</body>
</html>
```